Penny auction website for high end market

need a penny auction web design , requirement as below :-

- classy and noble, as i am only selli high end products
- 25 products for the main page , 5 products per row ( please see sample picture )
- top 5 products can be highlighted as those are limited edition products
- main page , products page, members page , faq and about us page
- matching logo with the name lotvo
- clean
- responsive for desktoop
-mobile version
Updates

i missed the mobile version, i should get the mobile version aswell, for desktop it should be responsive Added Wednesday, August 16, 2017

designer may use gold or silver color too as i am selling only high end products exclusively for members only, the layout can be different than the sample, it just a guide line for the sample, other better layout would be great to see and to have.

some idea how highend feel to me https://img.kravelshop.example/scr/51200/shining-gems-flash-cms-layout_52716-original.jpg

guys, please use this design https://www.pagewrenhub.example/flash-cms-layouts/52716.html as the base , i want it high class and up market, thanks

Target Market(s)

highend products buyer

Number of Pages Required

5+ page

Font styles to use
Serif
Sans Serif
Script
Other font styles liked:
• designer match it

Colors

Designer to choose colors to be used in the design.

Requirements
Must have
• source code, logos ( use lotvo for now, will change later when confirm ) , PSD
Nice to have
• more different type of designs would be great, designers can present they ideas other than my requirement

```html
<!DOCTYPE html>
<html lang="en">
<head>
<meta charset="utf-8">
<title>lotvo – Penny Auctions</title>
<link rel="stylesheet" href="https://fonts.googleapis.com/css2?family=Open+Sans:wght@400;600;700;800&display=swap">
<style>
  :root{
    --orange:#ef5a24;
    --dark:#3b3b3b;
    --page:#eeeeef;
    --white:#ffffff;
    --ink:#222222;
    --muted:#8a8a8a;
    --line:#cfcfcf;
    --green:#1ba532;
    --sold:#9a9a9a;
    --tone-dark-a:#4a4d55; --tone-dark-b:#1d1f24;
    --tone-silver-a:#e4e7ec; --tone-silver-b:#9da4ae;
    --tone-screen-a:#5f8fd4; --tone-screen-b:#2f4a2a;
    --tone-white-a:#fbfbfb; --tone-white-b:#c9cdd2;
    --tone-red-a:#d8332c; --tone-red-b:#6d1010;
    --tone-orange-a:#ffb066; --tone-orange-b:#f07c16;
  }
  *{margin:0;padding:0;box-sizing:border-box}
  html,body{width:1200px;height:2647px;overflow:hidden}
  body{position:relative;background:var(--page);font-family:"Open Sans",Arial,sans-serif;color:var(--ink)}

  /* header */
  .site-header{position:absolute;left:0;top:0;width:1200px;height:78px;background:var(--white)}
  .brand{position:absolute;font-weight:700;color:var(--orange);letter-spacing:-0.5px;line-height:1}
  .site-header .brand{left:132px;top:17px;font-size:38px}
  .main-nav{position:absolute;top:23px;left:418px;display:flex;align-items:center;height:25px}
  .main-nav a{font-size:11px;font-weight:700;color:var(--ink);text-decoration:none;text-transform:uppercase;margin-right:24px}
  .main-nav a.is-active{background:var(--orange);color:var(--white);padding:5px 10px;margin-right:24px}
  .search{position:absolute;left:909px;top:21px;width:157px;height:30px;border:1px solid var(--line);background:var(--white)}
  .search span{position:absolute;left:12px;top:8px;font-size:9px;color:var(--muted);font-weight:600}
  .search svg{position:absolute;right:10px;top:9px}

  /* hero */
  .hero{position:absolute;left:0;top:78px;width:1200px;height:624px;background:var(--page)}
  .hero-visual{position:absolute;left:168px;top:81px;width:838px;height:485px;border-radius:18px;
    background:radial-gradient(ellipse at 55% 40%,#6f8fb8 0%,#4c566a 45%,#2a2d33 75%,rgba(238,238,239,0) 100%)}
  .stat-badge{position:absolute;left:741px;top:35px;width:318px;height:108px;background:var(--white);
    border:1px solid var(--line);transform:rotate(-4deg);text-align:center;box-shadow:0 2px 6px rgba(0,0,0,.12)}
  .stat-badge strong{display:block;font-size:42px;font-weight:800;color:var(--orange);line-height:1;margin-top:14px}
  .stat-badge span{display:block;font-size:26px;font-weight:600;color:var(--dark);margin-top:4px;text-transform:uppercase}
  .badge-pin{position:absolute;left:734px;top:122px;width:10px;height:10px;border-radius:50%;background:var(--white);border:2px solid var(--muted)}

  /* steps band */
  .steps{position:absolute;left:0;top:702px;width:1200px;height:106px;background:var(--dark)}
  .step{position:absolute;top:0;height:106px;text-align:center}
  .step + .step{border-left:1px solid #555}
  .step-icon{position:absolute;left:50%;top:-41px;margin-left:-41px;width:82px;height:82px;border-radius:50%;
    background:var(--orange);border:6px solid var(--dark);display:flex;align-items:center;justify-content:center}
  .step-label{position:absolute;left:0;right:0;top:57px;font-size:11px;font-weight:700;color:var(--white);text-transform:uppercase}
  .cta{position:absolute;left:50%;top:50px;margin-left:-49px;width:98px;height:28px;background:var(--orange);color:var(--white);
    font-size:11px;font-weight:700;line-height:28px;text-transform:uppercase}

  /* auctions */
  .section-title{position:absolute;left:132px;top:860px;font-size:21px;font-weight:700;color:var(--orange);text-transform:uppercase}
  .auction-grid{position:absolute;left:131px;top:930px;width:950px;display:grid;
    grid-template-columns:repeat(5,185px);column-gap:6px;row-gap:9px}
  .lot{position:relative;height:276px;background:var(--white);text-align:center}
  .lot-photo{position:absolute;left:33px;top:20px;width:119px;height:108px;border-radius:10px}
  .tone-dark{background:linear-gradient(145deg,var(--tone-dark-a),var(--tone-dark-b))}
  .tone-silver{background:linear-gradient(145deg,var(--tone-silver-a),var(--tone-silver-b))}
  .tone-screen{background:linear-gradient(160deg,var(--tone-screen-a),var(--tone-screen-b))}
  .tone-white{background:linear-gradient(145deg,var(--tone-white-a),var(--tone-white-b))}
  .tone-red{background:linear-gradient(145deg,var(--tone-red-a),var(--tone-red-b))}
  .tone-orange{background:linear-gradient(145deg,var(--tone-orange-a),var(--tone-orange-b))}
  .lot-name{position:absolute;left:0;right:0;top:143px;font-size:13px;font-weight:600}
  .lot-price{position:absolute;left:0;right:0;top:168px;font-size:17px;color:var(--orange)}
  .lot-price sup{font-size:10px;vertical-align:6px}
  .lot-timer{position:absolute;left:57px;top:205px;width:71px;height:25px;border:1px solid var(--ink);
    font-size:12px;line-height:23px;letter-spacing:.5px}
  .lot-action{position:absolute;left:0;bottom:0;width:185px;height:28px;font-size:13px;font-weight:700;
    color:var(--white);line-height:28px;text-transform:uppercase;letter-spacing:.5px}
  .bid{background:var(--green)}
  .sold{background:var(--sold)}

  /* footer */
  .site-footer{position:absolute;left:0;top:2397px;width:1200px;height:250px;background:var(--dark)}
  .site-footer .brand{left:132px;top:52px;font-size:46px}
  .footer-head{position:absolute;top:56px;font-size:10px;font-weight:700;color:var(--white);text-transform:uppercase}
  .footer-menu{position:absolute;left:399px;top:85px;font-size:10px;color:#c8c8c8;text-transform:uppercase}
  .footer-menu span{margin:0 6px}
  .social{position:absolute;left:962px;top:83px;display:flex;gap:11px}
  .social i{display:block;width:28px;height:28px;border-radius:50%}
  .social .s1{background:#3b5ea8}.social .s2{background:#1da1e6}.social .s3{background:#e2533d}
  .footer-rule{position:absolute;left:132px;top:159px;width:936px;height:1px;background:#505050}
  .copyright{position:absolute;left:0;right:0;top:199px;text-align:center;font-size:10px;color:#b5b5b5}
</style>
</head>
<body>

<header class="site-header">
  <div class="brand">lotvo</div>
  <nav class="main-nav">
    <a class="is-active">Home</a>
    <a>All Auctions</a>
    <a>Show All Categories</a>
    <a>Services</a>
    <a>Contact Us</a>
  </nav>
  <div class="search">
    <span>SEARCH</span>
    <svg width="11" height="11" viewBox="0 0 11 11"><circle cx="4.5" cy="4.5" r="3.5" fill="none" stroke="#999" stroke-width="1.3"/><line x1="7" y1="7" x2="10" y2="10" stroke="#999" stroke-width="1.3"/></svg>
  </div>
</header>

<section class="hero">
  <div class="hero-visual" role="img" aria-label="Group of electronics: printer, monitor, laptops, tablets, phones, camera and mouse"></div>
  <div class="stat-badge"><strong>15895</strong><span>Finished Auctions</span></div>
  <div class="badge-pin"></div>
</section>

<section class="steps">
  <div class="step" style="left:0;width:353px">
    <div class="step-icon"><svg width="26" height="26" viewBox="0 0 26 26"><circle cx="13" cy="9" r="5" fill="#fff"/><path d="M4 23c0-5 4-8 9-8s9 3 9 8z" fill="#fff"/></svg></div>
    <div class="step-label">Create an Account</div>
  </div>
  <div class="step" style="left:353px;width:272px">
    <div class="step-icon"><svg width="30" height="30" viewBox="0 0 30 30"><circle cx="13" cy="13" r="9" fill="none" stroke="#fff" stroke-width="2.4"/><circle cx="13" cy="13" r="3" fill="#fff"/><path d="M16 16l10 4-4 1.5-1.5 4z" fill="#fff"/></svg></div>
    <div class="step-label">Choose Your Products</div>
  </div>
  <div class="step" style="left:625px;width:206px">
    <div class="step-icon"><svg width="30" height="28" viewBox="0 0 30 28"><path d="M4 10h22v15H4z" fill="#fff"/><path d="M2 5l13 4 13-4-3 5H5z" fill="#fff"/><rect x="13" y="10" width="4" height="15" fill="#ef5a24"/></svg></div>
    <div class="step-label">Bid and Win</div>
  </div>
  <div class="step" style="left:831px;width:220px">
    <div class="step-icon"><svg width="30" height="26" viewBox="0 0 30 26"><rect x="2" y="2" width="26" height="17" rx="2" fill="none" stroke="#fff" stroke-width="2.6"/><rect x="11" y="19" width="8" height="4" fill="#fff"/><rect x="8" y="22" width="14" height="2.5" fill="#fff"/></svg></div>
    <div class="cta">Start Now</div>
  </div>
</section>

<h2 class="section-title">Latest Posted Auctions</h2>

<main class="auction-grid">
  <article class="lot"><div class="lot-photo tone-dark" role="img" aria-label="Smartphone, front and back"></div><h3 class="lot-name">Pomela Phone</h3><p class="lot-price"><sup>$</sup>10.99</p><p class="lot-timer">00 : 02 : 10</p><div class="lot-action bid">Bid Now</div></article>
  <article class="lot"><div class="lot-photo tone-screen" role="img" aria-label="LED television showing a flower field"></div><h3 class="lot-name">LED Tv</h3><p class="lot-price"><sup>$</sup>8.99</p><p class="lot-timer">00 : 00 : 00</p><div class="lot-action sold">Sold</div></article>
  <article class="lot"><div class="lot-photo tone-dark" role="img" aria-label="DSLR camera"></div><h3 class="lot-name">Camera</h3><p class="lot-price"><sup>$</sup>2.99</p><p class="lot-timer">00 : 10 : 10</p><div class="lot-action bid">Bid Now</div></article>
  <article class="lot"><div class="lot-photo tone-silver" role="img" aria-label="Open laptop"></div><h3 class="lot-name">Laptop</h3><p class="lot-price"><sup>$</sup>10.99</p><p class="lot-timer">00 : 02 : 10</p><div class="lot-action bid">Bid Now</div></article>
  <article class="lot"><div class="lot-photo tone-dark" role="img" aria-label="Tablet and phone"></div><h3 class="lot-name">Slate Pad</h3><p class="lot-price"><sup>$</sup>10.99</p><p class="lot-timer">00 : 02 : 10</p><div class="lot-action bid">Bid Now</div></article>

  <article class="lot"><div class="lot-photo tone-dark" role="img" aria-label="Memory card"></div><h3 class="lot-name">Memory Card</h3><p class="lot-price"><sup>$</sup>10.99</p><p class="lot-timer">00 : 02 : 10</p><div class="lot-action bid">Bid Now</div></article>
  <article class="lot"><div class="lot-photo tone-dark" role="img" aria-label="Smartphone"></div><h3 class="lot-name">phone</h3><p class="lot-price"><sup>$</sup>8.99</p><p class="lot-timer">00 : 00 : 00</p><div class="lot-action sold">Sold</div></article>
  <article class="lot"><div class="lot-photo tone-silver" role="img" aria-label="Tablet on a stand"></div><h3 class="lot-name">tablet</h3><p class="lot-price"><sup>$</sup>2.99</p><p class="lot-timer">00 : 10 : 10</p><div class="lot-action bid">Bid Now</div></article>
  <article class="lot"><div class="lot-photo tone-dark" role="img" aria-label="DSLR camera"></div><h3 class="lot-name">Camera</h3><p class="lot-price"><sup>$</sup>10.99</p><p class="lot-timer">00 : 02 : 10</p><div class="lot-action sold">Sold</div></article>
  <article class="lot"><div class="lot-photo tone-silver" role="img" aria-label="USB card reader with chip"></div><h3 class="lot-name">Chip</h3><p class="lot-price"><sup>$</sup>10.99</p><p class="lot-timer">00 : 02 : 10</p><div class="lot-action bid">Bid Now</div></article>

  <article class="lot"><div class="lot-photo tone-silver" role="img" aria-label="Smartphone, front and back"></div><h3 class="lot-name">Pomela Phone</h3><p class="lot-price"><sup>$</sup>10.99</p><p class="lot-timer">00 : 02 : 10</p><div class="lot-action sold">Sold</div></article>
  <article class="lot"><div class="lot-photo tone-silver" role="img" aria-label="Laptop with accessories"></div><h3 class="lot-name">Laptop</h3><p class="lot-price"><sup>$</sup>8.99</p><p class="lot-timer">00 : 00 : 00</p><div class="lot-action sold">Sold</div></article>
  <article class="lot"><div class="lot-photo tone-white" role="img" aria-label="Washing machine"></div><h3 class="lot-name">Washingmachine</h3><p class="lot-price"><sup>$</sup>2.99</p><p class="lot-timer">00 : 10 : 10</p><div class="lot-action sold">Sold</div></article>
  <article class="lot"><div class="lot-photo tone-red" role="img" aria-label="Battery"></div><h3 class="lot-name">Battery</h3><p class="lot-price"><sup>$</sup>10.99</p><p class="lot-timer">00 : 02 : 10</p><div class="lot-action bid">Bid Now</div></article>
  <article class="lot"><div class="lot-photo tone-dark" role="img" aria-label="Wristwatch"></div><h3 class="lot-name">Watch</h3><p class="lot-price"><sup>$</sup>10.99</p><p class="lot-timer">00 : 02 : 10</p><div class="lot-action bid">Bid Now</div></article>

  <article class="lot"><div class="lot-photo tone-dark" role="img" aria-label="Smartwatch"></div><h3 class="lot-name">Pomela Phone</h3><p class="lot-price"><sup>$</sup>10.99</p><p class="lot-timer">00 : 02 : 10</p><div class="lot-action bid">Bid Now</div></article>
  <article class="lot"><div class="lot-photo tone-dark" role="img" aria-label="Folding tablet cover"></div><h3 class="lot-name">Cover</h3><p class="lot-price"><sup>$</sup>8.99</p><p class="lot-timer">00 : 00 : 00</p><div class="lot-action sold">Sold</div></article>
  <article class="lot"><div class="lot-photo tone-dark" role="img" aria-label="Leather phone wallet case"></div><h3 class="lot-name">Case</h3><p class="lot-price"><sup>$</sup>2.99</p><p class="lot-timer">00 : 10 : 10</p><div class="lot-action bid">Bid Now</div></article>
  <article class="lot"><div class="lot-photo tone-white" role="img" aria-label="Washing machine"></div><h3 class="lot-name">Washingmachine</h3><p class="lot-price"><sup>$</sup>10.99</p><p class="lot-timer">00 : 02 : 10</p><div class="lot-action sold">Sold</div></article>
  <article class="lot"><div class="lot-photo tone-silver" role="img" aria-label="Slim phone case"></div><h3 class="lot-name">Case</h3><p class="lot-price"><sup>$</sup>10.99</p><p class="lot-timer">00 : 02 : 10</p><div class="lot-action bid">Bid Now</div></article>

  <article class="lot"><div class="lot-photo tone-dark" role="img" aria-label="USB cable"></div><h3 class="lot-name">Cable</h3><p class="lot-price"><sup>$</sup>10.99</p><p class="lot-timer">00 : 02 : 10</p><div class="lot-action bid">Bid Now</div></article>
  <article class="lot"><div class="lot-photo tone-white" role="img" aria-label="Plug adapter"></div><h3 class="lot-name">Adapter</h3><p class="lot-price"><sup>$</sup>8.99</p><p class="lot-timer">00 : 00 : 00</p><div class="lot-action sold">Sold</div></article>
  <article class="lot"><div class="lot-photo tone-dark" role="img" aria-label="Home theatre speaker set"></div><h3 class="lot-name">Speaker</h3><p class="lot-price"><sup>$</sup>2.99</p><p class="lot-timer">00 : 10 : 10</p><div class="lot-action bid">Bid Now</div></article>
  <article class="lot"><div class="lot-photo tone-red" role="img" aria-label="Red over-ear headphones"></div><h3 class="lot-name">Headphone</h3><p class="lot-price"><sup>$</sup>10.99</p><p class="lot-timer">00 : 02 : 10</p><div class="lot-action bid">Bid Now</div></article>
  <article class="lot"><div class="lot-photo tone-orange" role="img" aria-label="Orange headphones"></div><h3 class="lot-name">Sonata Headphone</h3><p class="lot-price"><sup>$</sup>10.99</p><p class="lot-timer">00 : 02 : 10</p><div class="lot-action sold">Sold</div></article>
</main>

<footer class="site-footer">
  <div class="brand">lotvo</div>
  <div class="footer-head" style="left:399px">Menu</div>
  <div class="footer-menu">Home<span>|</span>All Auctions<span>|</span>Show All Categories<span>|</span>Services<span>|</span>Contact Us</div>
  <div class="footer-head" style="left:966px">Follow Us On</div>
  <div class="social"><i class="s1"></i><i class="s2"></i><i class="s3"></i></div>
  <div class="footer-rule"></div>
  <p class="copyright">Copyrights @ 2017 All Rights Reserved</p>
</footer>

</body>
</html>
```